Newyear letter A4 or A5 to be sent to our historic clients and prospects.

We have a poem, and want to create a new years card to remind our clients of our product range and wish them a merry Christmas and a happy new year. This brief is for a brand of high end dog fashion.
Product image can be found here: https://files.vantorabox.net/sh/p3wq7zt02mhxa4b/QTYP8hNcvlDk5R-MwePaUXoKa?dl=0
Our website: www.marlets.eu
The poem: https://sheets.brivondocs.net/document/d/7Kq2_RbWnLzP4eTjHxV9cMu_aYdG3sQpN8wFtBkZ/edit?usp=sharing

Target Market(s)

B2B Pet businesses: Pet boutiques, Retail chaines, Wholesalers, Distributors

Industry/Entity Type

Product

Requirements
Must have
• - Contain images from our collection
• - logo and baseline
• - Make the products pop

```html
<!DOCTYPE html>
<html lang="en">
<head>
<meta charset="utf-8">
<title>Marlets – Season's Greetings Card</title>
<link rel="stylesheet" href="https://fonts.googleapis.com/css2?family=Yellowtail&family=Montserrat:wght@500;600&family=Crimson+Text:ital@0;1&display=swap">
<style>
  :root {
    --backdrop: #f1ebe5;
    --paper: #ffffff;
    --gold: #c9a24a;
    --gold-deep: #a97f22;
    --gold-light: #e8cf8a;
    --band-top: #ffd27a;
    --band-mid: #f8ad32;
    --band-bottom: #f3a62a;
    --ink: #2f2a26;
    --brand-red: #c4262e;
    --flake-soft: #f4ede0;
    --flake-tint: #e9dcc2;
    --product-shadow: 0 8px 14px rgba(40, 30, 20, .35);
  }
  * { box-sizing: border-box; margin: 0; padding: 0; }
  html, body { width: 1200px; height: 800px; overflow: hidden; }
  body { background: var(--backdrop); position: relative; font-family: "Crimson Text", Georgia, serif; color: var(--ink); }

  /* ---------- Front card ---------- */
  .front-card {
    position: absolute; left: 40px; top: 170px; width: 560px; height: 460px;
    background: var(--paper); overflow: hidden;
    box-shadow: 0 6px 18px rgba(80, 60, 40, .18);
  }
  .front-card .flake-field {
    position: absolute; inset: 0 0 150px 0;
    background: radial-gradient(circle at 30% 40%, var(--flake-tint), var(--flake-soft) 60%, var(--paper));
  }
  .front-card .gold-band {
    position: absolute; left: 0; right: 0; top: 95px; height: 110px;
    background: linear-gradient(to bottom, var(--band-top), var(--band-mid) 45%, var(--band-bottom));
    border-top: 4px solid var(--gold-deep); border-bottom: 4px solid var(--gold-deep);
  }
  .greeting-label {
    position: absolute; left: 120px; top: 68px; width: 320px; height: 164px;
    background: var(--paper); border: 3px solid var(--gold);
    box-shadow: 0 3px 8px rgba(0,0,0,.15);
    overflow: hidden;
  }
  .greeting-label .kicker {
    font-family: "Montserrat", Arial, sans-serif; font-weight: 600;
    font-size: 15px; letter-spacing: .5px; color: var(--gold-deep);
    position: absolute; left: 50px; top: 36px;
  }
  .greeting-label .headline {
    font-family: "Yellowtail", "Brush Script MT", cursive; font-size: 64px; line-height: 1;
    color: var(--gold-deep); position: absolute; left: 0; right: 0; top: 58px;
    text-align: center; white-space: nowrap;
  }
  .front-card .product-row {
    position: absolute; left: 0; right: 0; bottom: 0; height: 175px;
  }
  .product { position: absolute; border-radius: 38% 42% 18% 18%; box-shadow: var(--product-shadow); }
  .product-black { left: 20px; bottom: -20px; width: 170px; height: 150px; background: linear-gradient(160deg, #f4f2ef 0 22%, #2a2a30 23%, #18181c); }
  .product-cream { left: 150px; bottom: 10px; width: 165px; height: 140px; background: linear-gradient(150deg, #f3efe6, #cfc6b4); }
  .product-pink  { left: 300px; bottom: 20px; width: 150px; height: 140px; background: linear-gradient(150deg, #f6dcdb, #c98584); }
  .product-taupe { left: 420px; bottom: 35px; width: 160px; height: 145px; background: linear-gradient(150deg, #b9ae9a, #6f6658); }

  /* ---------- Inside spread ---------- */
  .inside-card {
    position: absolute; left: 650px; top: 16px; width: 510px; height: 768px;
    background: var(--paper); box-shadow: 0 6px 18px rgba(80, 60, 40, .18);
  }
  .collage-panel {
    position: absolute; left: 0; top: 0; width: 510px; height: 370px;
    overflow: hidden;
    background: radial-gradient(circle at 60% 60%, var(--flake-tint), var(--flake-soft) 55%, var(--paper));
  }
  .collage-tile {
    position: absolute; width: 130px; height: 130px;
    border: 3px solid var(--gold); background: var(--paper);
    transform: rotate(-22deg);
    box-shadow: 0 4px 10px rgba(0,0,0,.18);
  }
  .collage-tile .photo { position: absolute; inset: 6px; background: #f7f5f2; }
  .collage-tile .photo::after {
    content: ""; position: absolute; left: 16%; right: 16%; top: 22%; bottom: 14%;
    border-radius: 40% 40% 16% 16%; box-shadow: var(--product-shadow);
    background: var(--item);
  }
  .tile-carrier-tan   { --item: linear-gradient(150deg, #e9c59c, #b07a48); }
  .tile-bag-cream     { --item: linear-gradient(150deg, #f4efe4, #c8bda8); }
  .tile-blanket-pink  { --item: linear-gradient(150deg, #f6d6d2, #d59c98); }
  .tile-dog-bed       { --item: linear-gradient(150deg, #f1d8b8, #b8895c); }
  .tile-basket-red    { --item: linear-gradient(150deg, #e0a1a1, #a8323a); }
  .tile-bag-grey      { --item: linear-gradient(150deg, #d9d2c8 0 25%, #b3b1b4 26%, #87858a); }
  .tile-jacket-black  { --item: linear-gradient(150deg, #d8cbb8 0 28%, #2b2c33 29%, #16161b); }
  .tile-dog-coat      { --item: linear-gradient(150deg, #ead7bd, #a97a4b); }
  .tile-gift-beige    { --item: linear-gradient(150deg, #f4ece0, #cdb999); }

  .brand-tile {
    position: absolute; left: 205px; top: 30px; width: 120px; height: 120px;
    border: 3px solid var(--gold); background: var(--paper);
    transform: rotate(-22deg);
    display: flex; align-items: center; justify-content: center;
  }
  .brand-name {
    font-family: "Crimson Text", Georgia, serif; font-size: 24px;
    color: var(--brand-red); transform: rotate(22deg);
  }

  .poem-panel {
    position: absolute; left: 0; top: 370px; width: 510px; height: 398px;
    border-top: 1px solid #e6e0d8;
  }
  .flake-accent { position: absolute; border-radius: 50%;
    background: radial-gradient(circle, var(--gold-light), transparent 70%); }
  .flake-accent.top { left: 30px; top: 20px; width: 60px; height: 60px; }
  .flake-accent.bottom { right: 40px; bottom: 20px; width: 60px; height: 60px; }

  .poem {
    position: absolute; left: 40px; top: 80px; right: 26px;
    display: grid; grid-template-columns: 1fr 1fr; column-gap: 22px;
    font-size: 12px; line-height: 1.38; white-space: nowrap;
  }
  .poem .stanza { margin-bottom: 14px; }
</style>
</head>
<body>

  <section class="front-card" aria-label="Card front">
    <div class="flake-field" role="img" aria-label="Gold snowflake pattern on white"></div>
    <div class="gold-band"></div>
    <div class="greeting-label">
      <span class="kicker">SEASON'S</span>
      <span class="headline">Greetings</span>
    </div>
    <div class="product-row">
      <div class="product product-black" role="img" aria-label="Black carrier bag with white fur trim"></div>
      <div class="product product-cream" role="img" aria-label="Cream toile quilted carrier"></div>
      <div class="product product-pink" role="img" aria-label="Pink toile quilted carrier"></div>
      <div class="product product-taupe" role="img" aria-label="Taupe toile quilted carrier"></div>
    </div>
  </section>

  <section class="inside-card" aria-label="Card inside">
    <div class="collage-panel" role="img" aria-label="Gold snowflake pattern with framed product photos">
      <div class="collage-tile tile-carrier-tan" style="left:20px; top:-20px;"><div class="photo" role="img" aria-label="Tan carrier with fur trim"></div></div>
      <div class="collage-tile tile-blanket-pink" style="left:-40px; top:110px;"><div class="photo" role="img" aria-label="Pink gift blanket"></div></div>
      <div class="collage-tile tile-bag-cream" style="left:95px; top:90px;"><div class="photo" role="img" aria-label="Cream shoulder bag"></div></div>
      <div class="collage-tile tile-dog-bed" style="left:25px; top:225px;"><div class="photo" role="img" aria-label="Small dog lying on a cushion"></div></div>
      <div class="brand-tile"><span class="brand-name">Marlets</span></div>
      <div class="collage-tile tile-basket-red" style="left:190px; top:215px;"><div class="photo" role="img" aria-label="Red patterned round basket"></div></div>
      <div class="collage-tile tile-bag-grey" style="left:305px; top:120px;"><div class="photo" role="img" aria-label="Grey carrier with fur trim"></div></div>
      <div class="collage-tile tile-jacket-black" style="left:410px; top:20px;"><div class="photo" role="img" aria-label="Black dog jacket with fur hood"></div></div>
      <div class="collage-tile tile-dog-coat" style="left:345px; top:260px;"><div class="photo" role="img" aria-label="Small dog wearing a beige coat"></div></div>
      <div class="collage-tile tile-gift-beige" style="left:455px; top:200px;"><div class="photo" role="img" aria-label="Beige gift set"></div></div>
    </div>

    <div class="poem-panel">
      <div class="flake-accent top" role="img" aria-label="Gold snowflake ornament"></div>
      <div class="poem">
        <div class="column">
          <p class="stanza">'Tis time for Christmas season come,<br>A time for celebration!<br>For feasts, for gifts, for warm spiced rum,<br>For carols and elation.</p>
          <p class="stanza">At Marlets we've all been busy,<br>Making gifts for special pets,<br>Snuggle baskets to make you dizzy,<br>Blankets, carriers and jackets.</p>
          <p class="stanza">We hope your pets are snug and warm,<br>In their brand new Marlets wear,<br>Safe from blistering winter storms,<br>Without worry or a care!</p>
        </div>
        <div class="column">
          <p class="stanza">And now I think our time is here,<br>To extend you many thanks,<br>Our hearts are filled with joyful cheer,<br>To have you in our ranks.</p>
          <p class="stanza">With many changes to our sector,<br>It's a wonderful affair,<br>Announcing our new director,<br>Welcome, Lena Vermeulen!</p>
          <p class="stanza">But for now we will say goodbye,<br>And leave you to your fun,<br>To your stockings and Christmas pies,<br>Happy Holidays everyone!</p>
        </div>
      </div>
      <div class="flake-accent bottom" role="img" aria-label="Gold snowflake ornament"></div>
    </div>
  </section>

</body>
</html>
```